Vela Errands Web Design Project

Homepage components
o Logo
o Rotating header
o Main menu
o Animation video
o Banners
o Members login
o Latest news

The design’s preferred colors are black (background), silver (main tabs) and white (text)

Site map:
• Home
• News
• About us
o Welcome Note
o Company Profile
• Member Log in
o Registered homepage
? Request a service (form)
? Services directory
? Update profile
? Services history
• Member registration
o Registration form
• Partners
Footer Menu
• Contact us
• Terms & Conditions
• Privacy policy
• Social media links
• Sitemap

Brief about the company:
Vela Errands is a Jordanian company dedicated to elevate and redefine the level of service in the country. We are set out to give premium services at affordable prices. In this fast paced environment that we live in, we barely have the luxury of free time anymore and we, at Vela Errands will be giving you that extra hour or two per day to spend as your heart desires!
By becoming a member you will get access to a world of comfort and peace of mind. We have done the homework on your behalf and have established the network of connections that will enable you to live a headache free life.
We will be providing our members with support and assistance in their day to day lives in the fields that consumes and wastes time the most. We are value driven and below is our “ever-growing” list of services that we will provide at excellent prices:
• Maintenance (carpentry, plumbing, electrical, painting, decorating, gardening… etc)
• Cleaning (pre and post tenancy, periodical deep cleaning, packing and moving services, laundry… etc)
• Personalized delivery services (grocery, important documents, office related supplies, posting cheques, food, paying bills… etc)
• Passport, driving license and ID reissuance
• Travel arrangements (flights, hotels, airport transfers… etc)
• Premium car rental services
• Restaurant reservations
• IT assistance
• Event planning and all related services
• Catering arrangements

Aside from all the services we have on offer we have collaborated with a number of places (that we like to call partners) in town where Vela Errands members are entitled to benefits and privileges that will most certainly add value to their membership. Alongside our partners we have come up with the best formula that will please our members. Below are some of our current partners:

Requirements
Must have
• Homepage components
o Logo
o Rotating header
o Main menu
o Animation video
o Banners
o Members login
o Latest news

```html
<!DOCTYPE html>
<html lang="en">
<head>
<meta charset="utf-8">
<title>Vela Errands – Home</title>
<link rel="stylesheet" href="https://fonts.googleapis.com/css2?family=Barlow:wght@400;500&family=Encode+Sans+Condensed:wght@400&family=Lato:wght@400&display=swap">
<style>
:root{
  --page:#2a2627;
  --panel:#171415;
  --header:#d3d6d6;
  --search:#e6ebea;
  --tab:#3f3d3c;
  --text:#ffffff;
  --muted:#d8d8d8;
  --lime:#c6f000;
  --link:#9fa56a;
  --footer:#0d0c0c;
  --arrow:#7fa8d8;
}
*{box-sizing:border-box;margin:0;padding:0}
html,body{width:1200px;height:1158px;overflow:hidden;background:var(--page)}
body{position:relative;font-family:"Barlow",sans-serif;color:var(--text)}
.abs{position:absolute}
.topstrip{left:0;top:0;width:1200px;height:9px;background:#6a6668}
.utility{right:33px;top:21px;display:flex;gap:16px;font-size:15px;letter-spacing:.5px}
.utility span,.bullets li{display:flex;align-items:center;gap:6px}
.arrow{width:11px;height:13px;flex:none}
.masthead{left:20px;top:51px;width:1160px;height:131px;background:var(--header);border-radius:8px 8px 0 0}
.brand{left:54px;top:24px;display:flex;align-items:center;gap:12px}
.brand-mark{width:22px;height:22px;border-radius:50%;background:#2a2627}
.brand-name{font-family:"Barlow",sans-serif;font-size:44px;font-weight:500;color:#2a2627;letter-spacing:1px}
.tagline{left:78px;top:75px;font-size:18px;letter-spacing:2px;color:#fff}
.search{left:826px;top:46px;width:246px;height:35px;background:var(--search);border-radius:7px;padding:8px 18px;font-size:14px;color:#8f9a98;letter-spacing:1px}
.search-icon{left:1078px;top:40px}
.menu{left:0;top:182px;width:1200px;height:40px;background:linear-gradient(#403d3d,#141212 70%,#070606)}
.menu-item{top:10px;font-size:15.5px;letter-spacing:1px;color:#f2f2f2}
.menu-sep{top:4px;width:1px;height:32px;background:#6b6767}
.new-account{left:1005px;top:7px;width:175px;height:30px;border-radius:6px;background:linear-gradient(#5b5859,#2f2c2d);font-size:14.5px;letter-spacing:.8px;padding:7px 0 0 46px}
.new-account svg{position:absolute;left:8px;top:-12px}
.hero{left:98px;top:234px;width:992px;height:358px;border-radius:8px;overflow:hidden;background:linear-gradient(90deg,#1b1a1a 0%,#0f0f0f 48%,#3a3a3a 62%,#8a949a 76%,#b9c2c7 100%)}
.hero-photo{position:absolute;left:500px;top:0;width:492px;height:358px;background:radial-gradient(ellipse at 55% 40%,rgba(140,160,180,.65),rgba(60,70,80,0) 60%),linear-gradient(180deg,rgba(210,215,220,.5),rgba(90,100,105,.55))}
.hero-title{left:40px;top:70px;font-family:"Encode Sans Condensed",sans-serif;font-size:32px;letter-spacing:.3px}
.hero-copy{left:61px;top:133px;width:540px;font-size:14.5px;line-height:22px;letter-spacing:.5px}
.read-more{left:435px;top:219px;width:134px;height:38px;border-radius:6px;background:#4a4445;font-size:12.5px;letter-spacing:1px;text-align:center;line-height:38px}
.pager{left:1090px;top:422px;width:37px;height:149px;background:#121111;border:1px solid #3a3838}
.pager i{position:absolute;left:6px;width:23px;height:23px;border-radius:50%;background:#555}
.pager i.on{background:var(--lime)}
.pager-pointer{left:1080px;top:473px}
.card{top:602px;height:365px;background:var(--panel);border-radius:7px}
.card-tab{top:2px;height:37px;background:var(--tab);border-radius:0 0 6px 6px;font-size:18px;letter-spacing:1px;text-align:center;line-height:36px}
.corner{width:14px;height:9px;background:var(--lime)}
.news-date{font-size:12.5px;letter-spacing:.5px;text-align:right;width:250px}
.news-text{width:260px;font-size:12.5px;line-height:19px;letter-spacing:.5px}
.intro{left:24px;top:60px;width:256px;font-size:12.5px;line-height:19px;letter-spacing:.5px}
.bullets{list-style:none;font-size:13.5px;letter-spacing:.6px;line-height:25px}
.quote{left:10px;width:230px;font-size:12px;line-height:14px;letter-spacing:.4px}
.quote-by{left:10px;font-size:12px;letter-spacing:.6px}
.dashes{left:20px;width:204px;border-top:1px dashed #777}
.footer{left:19px;top:964px;width:1160px;height:194px;background:var(--footer)}
.footer h3{position:absolute;top:40px;font-family:"Lato",sans-serif;font-weight:400;font-size:24px}
.footer ul{position:absolute;top:88px;list-style:none;font-size:12.5px;letter-spacing:.6px;color:var(--link);line-height:25px}
.footer li::before{content:"›";color:#ccc;margin-right:9px;font-size:11px}
.follow{left:948px;top:60px;font-size:24px;letter-spacing:1px}
.social{left:895px;top:89px;width:232px;height:65px;background:#000;border-radius:6px;border:1px solid #222}
.social i{position:absolute;top:16px;width:33px;height:33px;border-radius:50%}
</style>
</head>
<body>
<svg width="0" height="0" style="position:absolute">
  <defs>
    <symbol id="chevron" viewBox="0 0 11 13"><path d="M1 1 L10 6.5 L1 12 L4 6.5 Z" fill="var(--arrow)"/></symbol>
  </defs>
</svg>

<div class="abs topstrip"></div>
<nav class="abs utility">
  <span><svg class="arrow"><use href="#chevron"/></svg>Login</span>
  <span><svg class="arrow"><use href="#chevron"/></svg>Help</span>
  <span><svg class="arrow"><use href="#chevron"/></svg>FAQS</span>
</nav>

<header class="abs masthead">
  <div class="abs brand"><span class="brand-mark"></span><span class="brand-name">Vela Errands</span></div>
  <div class="abs tagline">We make life easier</div>
  <div class="abs search">Search</div>
  <svg class="abs search-icon" width="40" height="40" viewBox="0 0 40 40">
    <circle cx="16" cy="16" r="12" fill="#dfe9f2" stroke="#8a98a6" stroke-width="3"/>
    <line x1="25" y1="25" x2="36" y2="36" stroke="#555" stroke-width="5" stroke-linecap="round"/>
  </svg>
</header>

<nav class="abs menu">
  <span class="abs menu-item" style="left:20px">Home</span>
  <span class="abs menu-sep" style="left:89px"></span>
  <span class="abs menu-item" style="left:104px">About us</span>
  <span class="abs menu-sep" style="left:190px"></span>
  <span class="abs menu-item" style="left:210px">Member registration</span>
  <span class="abs menu-sep" style="left:381px"></span>
  <span class="abs menu-item" style="left:408px">Partners</span>
  <span class="abs menu-sep" style="left:493px"></span>
  <span class="abs menu-item" style="left:516px">Contact us</span>
  <div class="abs new-account">
    <svg width="34" height="36" viewBox="0 0 34 36"><circle cx="14" cy="9" r="7" fill="#4a8fd8"/><path d="M2 32 Q14 10 26 32 Z" fill="#3a7ccc"/><path d="M20 28 L30 14 L33 17 L23 31 Z" fill="#f0a020"/></svg>
    New Account
  </div>
</nav>

<section class="abs hero">
  <div class="hero-photo" role="img" aria-label="Photo of cupped hands holding a glass globe above rippling water"></div>
  <h1 class="abs hero-title" style="font-weight:400">Vela Errands is a Jordanian company</h1>
  <p class="abs hero-copy">We are set out to give premium services at affordable prices. In this fast paced environment that we live in, we barely have the luxury of free time anymore and we, at Vela Errands will be giving you that extra hour or two per day to spend as your heart desires</p>
  <div class="abs read-more">Read More</div>
</section>
<svg class="abs pager-pointer" width="8" height="12" viewBox="0 0 8 12"><path d="M0 0 L8 6 L0 12 Z" fill="var(--lime)"/></svg>
<div class="abs pager"><i style="top:12px"></i><i class="on" style="top:44px"></i><i style="top:74px"></i><i style="top:106px"></i></div>

<section class="abs card" style="left:20px;width:287px">
  <div class="abs card-tab" style="left:54px;width:141px">Latest News</div>
  <div class="abs news-date" style="left:12px;top:48px">10/10/12</div>
  <p class="abs news-text" style="left:18px;top:68px">Lorem ipsum dolor sit amet, consectetuer adipiscing</p>
  <div class="abs news-date" style="left:12px;top:117px">10/10/12</div>
  <p class="abs news-text" style="left:19px;top:137px">Lorem ipsum dolor sit amet, consectetuer adipiscing</p>
  <div class="abs news-date" style="left:14px;top:191px">10/10/12</div>
  <p class="abs news-text" style="left:20px;top:211px">Lorem ipsum dolor sit amet, consectetuer adipiscing</p>
  <div class="abs news-date" style="left:15px;top:272px">10/10/12</div>
  <p class="abs news-text" style="left:21px;top:293px">Lorem ipsum dolor sit amet, consectetuer adipiscing</p>
</section>
<div class="abs corner" style="left:307px;top:941px"></div>

<section class="abs card" style="left:323px;width:286px">
  <div class="abs card-tab" style="left:59px;width:172px">Why Choose Us?</div>
  <p class="abs intro">Lorem ipsum dolor sit amet, consectetuer adipiscingLorem ipsum dolor sit amet, consectetuer adipiscingLorem ipsum dolor sit amet, consectetuer adipiscing</p>
  <ul class="abs bullets" style="left:35px;top:168px">
    <li><svg class="arrow"><use href="#chevron"/></svg>Lorem ipsum dolor consectetuer</li>
    <li><svg class="arrow"><use href="#chevron"/></svg>Adipiscing elit, diam nonummy</li>
    <li><svg class="arrow"><use href="#chevron"/></svg>Nibh euismod tincidunt laoreet</li>
    <li><svg class="arrow"><use href="#chevron"/></svg>Dolore magna aliquam volutpat</li>
    <li><svg class="arrow"><use href="#chevron"/></svg>Ut wisi enim ad minim veniam</li>
  </ul>
</section>
<div class="abs corner" style="left:609px;top:941px"></div>

<section class="abs card" style="left:623px;width:288px">
  <div class="abs card-tab" style="left:51px;width:171px">Our Services</div>
  <ul class="abs bullets" style="left:20px;top:59px">
    <li><svg class="arrow"><use href="#chevron"/></svg>Lorem ipsum dolor consectetuer</li>
    <li><svg class="arrow"><use href="#chevron"/></svg>Adipiscing elit, diam nonummy</li>
    <li><svg class="arrow"><use href="#chevron"/></svg>Nibh euismod tincidunt laoreet</li>
    <li><svg class="arrow"><use href="#chevron"/></svg>Dolore magna aliquam volutpat</li>
    <li><svg class="arrow"><use href="#chevron"/></svg>Ut wisi enim ad minim veniam</li>
  </ul>
  <ul class="abs bullets" style="left:23px;top:196px">
    <li><svg class="arrow"><use href="#chevron"/></svg>Lorem ipsum dolor consectetuer</li>
    <li><svg class="arrow"><use href="#chevron"/></svg>Adipiscing elit, diam nonummy</li>
    <li><svg class="arrow"><use href="#chevron"/></svg>Nibh euismod tincidunt laoreet</li>
    <li><svg class="arrow"><use href="#chevron"/></svg>Dolore magna aliquam volutpat</li>
    <li><svg class="arrow"><use href="#chevron"/></svg>Ut wisi enim ad minim veniam</li>
  </ul>
</section>
<div class="abs corner" style="left:911px;top:941px"></div>

<aside class="abs card" style="left:923px;width:257px;height:362px">
  <p class="abs quote" style="top:28px">“Lorem ipsum dolor amet, consectetuer adipiscing elit, sed diam nonummy.”</p>
  <div class="abs quote-by" style="top:68px">Ana Rell</div>
  <div class="abs dashes" style="top:107px"></div>
  <p class="abs quote" style="top:129px">“Lorem ipsum dolor amet, consectetuer adipiscing elit, sed diam nonummy.”</p>
  <div class="abs quote-by" style="top:169px">Ana Rell</div>
  <div class="abs dashes" style="top:222px;left:23px"></div>
  <p class="abs quote" style="top:253px">“Lorem ipsum dolor amet, consectetuer adipiscing elit, sed diam nonummy.”</p>
  <div class="abs quote-by" style="top:293px">Ana Rell</div>
</aside>

<footer class="abs footer">
  <h3 style="left:41px">About Us</h3>
  <ul style="left:40px"><li>Lorem ipsum dolo</li><li>Lorem ipsum dolo</li><li>Lorem ipsum dolo</li></ul>
  <h3 style="left:208px">Advice</h3>
  <ul style="left:207px;top:86px"><li>Lorem ipsum dolo</li><li>Lorem ipsum dolo</li><li>Lorem ipsum dolo</li></ul>
  <h3 style="left:375px">Join In</h3>
  <ul style="left:374px"><li>Lorem ipsum dolo</li><li>Lorem ipsum dolo</li><li>Lorem ipsum dolo</li></ul>
  <h3 style="left:541px">Downloads</h3>
  <ul style="left:540px;top:87px"><li>Lorem ipsum dolo</li><li>Lorem ipsum dolo</li><li>Lorem ipsum dolo</li></ul>
  <div class="abs follow">Follow Us</div>
  <div class="abs social" aria-label="Social media links">
    <i style="left:30px;background:#4fb6e6"></i>
    <i style="left:78px;background:#4a66a0"></i>
    <i style="left:126px;background:#e8e8ea"></i>
    <i style="left:175px;background:#f08a1c"></i>
  </div>
</footer>
</body>
</html>
```